luxury contemporary fashion website needs simple, elegant flowchart to describe the buying and selli

* Luxury, resale, preloved items are sold on this online platform
*Horizontal, simple, flowchart with 5 steps in 'friendly' font with a simple emoticon/ picture for each step
*To be positioned in the 'How we work' tab of the webpage to explain in a very simple manner the buying and selling process for the customers.
*Attached is a very rudimentary mock-up of what we would like included and an idea of a project similar to what we desire
* to confirm the text for each step, we have also attached a word file below

Industry/Entity Type

Fashion

Font styles to use
Sans Serif

Colors
86cfc6
cfeae6

Requirements
Must have
• Simple drawing / shape after each point In the closest to 'duck egg blue' fill colour you can find with a black outline

```html
<!DOCTYPE html>
<html lang="en">
<head>
<meta charset="utf-8">
<title>How we work</title>
<link rel="stylesheet" href="https://fonts.googleapis.com/css2?family=Urbanist:wght@400;500;600;700&display=swap">
<style>
  :root {
    --mint: #86cfc6;
    --duck-egg: #cfeae6;
    --chevron: #d6eeea;
    --ink: #2f2f2f;
    --ink-soft: #4a4a4a;
    --paper: #ffffff;
  }
  * { margin: 0; padding: 0; box-sizing: border-box; }
  html, body { width: 1200px; height: 758px; overflow: hidden; background: var(--paper); }
  body { font-family: "Urbanist", sans-serif; color: var(--ink); }
  .flow { position: relative; width: 1200px; height: 758px; }
  .flow-shapes { position: absolute; inset: 0; }
  .step-label { position: absolute; transform: translateX(-50%); text-align: center; white-space: nowrap; }
  .step-title { font-size: 16.5px; font-weight: 600; line-height: 1.2; margin-bottom: 3px; }
  .step-title.is-muted { color: var(--ink-soft); }
  .step-text { font-size: 11.5px; font-weight: 500; line-height: 1.2; }
  .badge-number { font-family: "Urbanist", sans-serif; font-size: 21px; font-weight: 500; fill: var(--paper); }
  .payment-text { font-family: "Urbanist", sans-serif; font-size: 21px; font-weight: 500; fill: var(--paper); }
  .currency-text { font-family: "Urbanist", sans-serif; font-weight: 700; fill: var(--mint); }
</style>
</head>
<body>
<main class="flow">
  <svg class="flow-shapes" width="1200" height="758" viewBox="0 0 1200 758" xmlns="http://www.w3.org/2000/svg">
    <!-- chevrons -->
    <g fill="none" stroke="var(--chevron)" stroke-width="4">
      <polyline points="238,348 257,372 238,396"/>
      <polyline points="434,348 453,372 434,396"/>
      <polyline points="636,348 655,372 636,396"/>
    </g>

    <!-- step circles -->
    <g fill="var(--duck-egg)" stroke="var(--mint)" stroke-width="1.5">
      <circle cx="147" cy="365" r="58"/>
      <circle cx="344" cy="365" r="58"/>
      <circle cx="547" cy="363" r="58"/>
      <circle cx="741" cy="363" r="59"/>
      <circle cx="1060" cy="203" r="62"/>
      <circle cx="1052" cy="443" r="60"/>
    </g>

    <!-- step icons -->
    <rect x="108" y="335" width="80" height="62" rx="14" fill="var(--mint)" role="img" aria-label="Clothing, handbag, sunglasses and watch"/>
    <rect x="306" y="340" width="78" height="46" rx="20" fill="var(--mint)" role="img" aria-label="Delivery scooter"/>
    <g role="img" aria-label="Shopping bag with magnifying glass">
      <rect x="528" y="338" width="42" height="54" rx="3" fill="var(--mint)"/>
      <circle cx="560" cy="372" r="13" fill="var(--duck-egg)" stroke="#555" stroke-width="5"/>
      <line x1="569" y1="382" x2="580" y2="393" stroke="#555" stroke-width="6" stroke-linecap="round"/>
    </g>
    <path class="plane" fill="var(--mint)" d="M764 341c4-4 7-3 5 2l-10 15 9 26-5 4-14-21-10 9 1 9-4 3-5-11-11-6 3-4 9 1 9-10-21-14 4-5 26 9z"/>

    <!-- payment -->
    <circle cx="902" cy="361" r="60" fill="var(--mint)" stroke="var(--duck-egg)" stroke-width="2"/>
    <text class="payment-text" x="903" y="352" text-anchor="middle">Your</text>
    <text class="payment-text" x="903" y="380" text-anchor="middle">Payment</text>

    <!-- branch arrows -->
    <g fill="none" stroke="var(--mint)" stroke-width="7">
      <path d="M955 340 C955 320 962 306 972 298"/>
      <path d="M955 382 C955 400 962 412 972 419"/>
    </g>
    <polygon points="962,292 982,291 975,310" fill="var(--mint)"/>
    <polygon points="962,425 982,426 975,407" fill="var(--mint)"/>

    <!-- currency -->
    <text class="currency-text" x="1012" y="216" font-size="46">$</text>
    <text class="currency-text" x="1038" y="228" font-size="58">£</text>
    <text class="currency-text" x="1076" y="216" font-size="38" font-weight="400">€</text>

    <!-- charity -->
    <rect x="1018" y="420" width="66" height="50" rx="20" fill="var(--mint)" role="img" aria-label="Hands holding a heart"/>

    <!-- number badges -->
    <g fill="var(--mint)">
      <circle cx="113" cy="317" r="18"/>
      <circle cx="306" cy="317" r="18"/>
      <circle cx="502" cy="317" r="18"/>
      <circle cx="699" cy="317" r="18"/>
      <circle cx="849" cy="318" r="18" stroke="var(--duck-egg)" stroke-width="3"/>
    </g>
    <text class="badge-number" x="113" y="325" text-anchor="middle">1</text>
    <text class="badge-number" x="306" y="325" text-anchor="middle">2</text>
    <text class="badge-number" x="502" y="325" text-anchor="middle">3</text>
    <text class="badge-number" x="699" y="325" text-anchor="middle">4</text>
    <text class="badge-number" x="849" y="326" text-anchor="middle">5</text>

    <!-- small accents -->
    <g fill="var(--mint)">
      <polygon points="224,471 225.5,474 229,474 226,476 227,479 224,477 221,479 222,476 219,474 222.5,474"/>
      <polygon points="221,479 222,481 224,481 222.5,482.5 223,485 221,483.5 219,485 219.5,482.5 218,481 220,481"/>
      <polygon points="230,479 231,481 233,481 231.5,482.5 232,485 230,483.5 228,485 228.5,482.5 227,481 229,481"/>
      <path d="M427 507c-3-2-6-4-6-7a3 3 0 0 1 6-1 3 3 0 0 1 6 1c0 3-3 5-6 7z"/>
      <circle cx="1128" cy="542" r="7"/>
    </g>
    <polyline points="600,500 604,504 611,497" fill="none" stroke="var(--mint)" stroke-width="2.2"/>
    <rect x="1112" y="309" width="18" height="12" rx="2" fill="none" stroke="var(--mint)" stroke-width="1.2"/>
    <line x1="1112" y1="313" x2="1130" y2="313" stroke="var(--mint)" stroke-width="1.5"/>
  </svg>

  <div class="step-label" style="left:147px; top:433px;">
    <p class="step-title">Have items to sell?</p>
    <p class="step-text">brand spanking or nearly new</p>
  </div>
  <div class="step-label" style="left:345px; top:433px;">
    <p class="step-title">Personal collection</p>
    <p class="step-text">we come to you to collect<br>the pieces we know<br>thelumera customers will love</p>
  </div>
  <div class="step-label" style="left:549px; top:432px;">
    <p class="step-title is-muted">We prepare</p>
    <p class="step-text">your item for sale with thorough<br>authenticity &amp; condition checks...<br>so you don't have to!</p>
  </div>
  <div class="step-label" style="left:742px; top:432px;">
    <p class="step-title">Once sold</p>
    <p class="step-text">we lovingly prepare the item<br>shipped via tracked services</p>
  </div>
  <div class="step-label" style="left:1062px; top:271px;">
    <p class="step-title">Pocket your cash</p>
    <p class="step-text">get amount for your item</p>
  </div>
  <div class="step-label" style="left:1052px; top:512px;">
    <p class="step-title">Donate to charity</p>
    <p class="step-text">full or partial amount</p>
  </div>
</main>
</body>
</html>
```